Velmora Business Card

We need a design for business cards for our new company. We are a resident safety and security company company that focuses on senior living communities. we provide Nurse call, Access control, CCTV, Wired and wireless network infrastructure, Wander Management, and much more!

Our logo is the circuit board shield. Representing our high tech security solutions. I would like the business card to bring the same theme with perhaps some circuit board traces around the card similar to our logo

```html
<!DOCTYPE html>
<html lang="en">
<head>
<meta charset="utf-8">
<title>Velmora Business Card</title>
<link rel="stylesheet" href="https://fonts.googleapis.com/css2?family=Tinos:wght@400;700&family=Arimo:wght@400&display=swap">
<style>
  :root {
    --page: #e4e4e4;
    --card-white: #ffffff;
    --brand-blue: #0b5fd0;
    --blue-deep: #0a4fc9;
    --blue-light: #0a9ae6;
    --sky: #1ab0f0;
    --grey-band: #7d7d7d;
    --text-grey: #555555;
  }
  * { margin: 0; padding: 0; box-sizing: border-box; }
  html, body { width: 1200px; height: 1200px; overflow: hidden; background: var(--page); }
  .canvas { position: relative; width: 1200px; height: 1200px; }
  .card {
    position: absolute; left: 257px; width: 686px; height: 392px;
    border-radius: 22px; overflow: hidden;
  }
  .card-front { top: 158px; background: var(--card-white); }
  .card-back {
    top: 653px;
    background: radial-gradient(ellipse at 50% 45%, var(--sky) 0%, var(--blue-light) 35%, var(--blue-deep) 100%);
  }
  .front-shapes { position: absolute; inset: 0; }
  .wordmark {
    position: absolute; font-family: "Tinos", serif; font-weight: 400;
    letter-spacing: 1px; text-transform: uppercase;
  }
  .front-wordmark { left: 48px; top: 176px; font-size: 38px; color: var(--brand-blue); }
  .back-wordmark { left: 0; right: 0; top: 228px; text-align: center; font-size: 50px; color: #fff; }
  .holder { position: absolute; right: 68px; top: 182px; text-align: right; }
  .holder-name {
    font-family: "Tinos", serif; font-weight: 700; font-size: 27px;
    color: var(--brand-blue); letter-spacing: 1px; line-height: 1;
  }
  .holder-role { font-family: "Arimo", sans-serif; font-size: 14px; color: var(--text-grey); margin-top: 6px; }
  .contacts { position: absolute; left: 48px; top: 262px; list-style: none; }
  .contacts li {
    display: flex; align-items: center; gap: 10px; height: 20.5px;
    font-family: "Arimo", sans-serif; font-size: 16px; color: var(--text-grey);
  }
  .contacts svg { width: 16px; height: 16px; flex: none; fill: var(--brand-blue); }
</style>
</head>
<body>
<div class="canvas">
  <section class="card card-front">
    <svg class="front-shapes" viewBox="0 0 686 392" aria-hidden="true">
      <defs>
        <linearGradient id="swoosh" x1="0" y1="0" x2="0" y2="1">
          <stop offset="0" stop-color="#0a9ae6"/>
          <stop offset="1" stop-color="#0a4fc9"/>
        </linearGradient>
      </defs>
      <path d="M552,0 H686 V392 H497 Z" fill="var(--grey-band)"/>
      <path d="M622,58 C668,120 690,220 686,392 H497 Z" fill="url(#swoosh)" stroke="#fff" stroke-width="3"/>
      <path d="M0,0 H552 C640,40 680,140 650,240 C620,320 560,360 497,392 H0 Z" fill="var(--card-white)"/>
    </svg>
    <div class="wordmark front-wordmark">Velmora</div>
    <div class="holder">
      <div class="holder-name">OWEN MARLETT</div>
      <div class="holder-role">President</div>
    </div>
    <ul class="contacts">
      <li><svg viewBox="0 0 16 16"><path d="M3 1l3 3-1.5 2a9 9 0 0 0 5.5 5.5L12 10l3 3-2 2C7 15 1 9 1 3z"/></svg>(555) 014-2270</li>
      <li><svg viewBox="0 0 16 16"><path d="M4 0h8v16H4zM5.5 2v10h5V2zM7 13.5h2v1H7z" fill-rule="evenodd"/></svg>(555) 018-4431</li>
      <li><svg viewBox="0 0 16 16"><path d="M1 4h14v9H1zM1.5 4.5L8 9.5l6.5-5" /></svg>Owen@Velmora.com</li>
      <li><svg viewBox="0 0 16 16"><circle cx="8" cy="8" r="7"/><path d="M4 5c2 0 3 1 2 3s1 3 0 5M10 2c0 2 2 2 3 3" stroke="#fff" stroke-width="1.2" fill="none"/></svg>www.Velmora.com</li>
    </ul>
  </section>

  <section class="card card-back">
    <div class="wordmark back-wordmark">Velmora</div>
  </section>
</div>
</body>
</html>
```